Trade fair QRVLN business card 7” x 5”

QRVLN exhibits on technology-hospitality trade fair in the UK this year. Therefore we are looking for well-designed marketing card (examples are linked in the bottom). The main role of these materials is to attract receivers to visit our website & find out more about QRVLN solutions.
Preferred used colours: white, various blue tints, black.
The front should contain branding & motto (“Modern beverage stocktaking”). Logotypes are attached.
The back should contain:
(value proposition),
Modern technology solution for beverage stocktaking
Accurate & effective stocktaking
Swift measuring with 99% accuracy makes stocktaking significantly quicker and more cost effective (or cost optimising).
Software solution supported with/by hardware tools
QRVLN system is based on universally accessible platforms - smartphones, PCs, and laptops. Your main measuring tool, smart scale, is delivered by QRVLN.
Smart & simple reporting system
Data availability - everywhere, anytime
Useful functions help stock managing at your bar
(call to action),
Find us on qrvln-example.com and try QRVLN with a one-month free trial.
(promo code)
Claim your 50% off discount with above promo code
Marketing card examples:
https://www.plinvoro-example.com/Which-startup-has-the-best-brochure-in-terms-of-design-and-content
Target Market(s)
QRVLN solution was created to help bar owners, bar managers and head bartenders to make their stocktaking process swift & accurate. Therefore, our product is targeting every business which sells portioned beverages.
Industry/Entity Type
Information Technology
Font styles to use
Look and feel
Each slider illustrates characteristics of the customer's brand and the style your logo design should communicate.

```html
<!DOCTYPE html>
<html lang="en">
<head>
<meta charset="utf-8">
<title>QRVLN trade fair card</title>
<link rel="stylesheet" href="https://fonts.googleapis.com/css2?family=Kanit:wght@400;500;600&family=Lato:wght@400;700&display=swap">
<style>
  :root {
    --teal: #23ad97;
    --blue: #1b4fa3;
    --navy: #163a8c;
    --paper: #f3f5f6;
    --tint: #e7ebee;
    --ink: #1d1f24;
    --white: #ffffff;
    --stage: #d8f7f0;
  }
  * { box-sizing: border-box; margin: 0; padding: 0; }
  html, body { width: 1200px; height: 1035px; overflow: hidden; background: var(--stage); }
  body { position: relative; font-family: "Lato", sans-serif; color: var(--ink); }

  .card {
    position: absolute; left: 250px; width: 700px; height: 500px;
    border-radius: 14px; overflow: hidden; background: var(--paper);
    box-shadow: 0 6px 18px rgba(20, 60, 70, .18);
  }
  .card--back { top: 12px; }
  .card--front { top: 523px; }

  /* Back */
  .back__header {
    position: absolute; left: 0; top: 22px; width: 100%; height: 98px;
    background: var(--teal); border-bottom: 4px solid var(--navy);
    padding: 8px 0 0 34px;
  }
  .back__title {
    font-family: "Kanit", sans-serif; font-weight: 500; color: var(--white);
    font-size: 34px; line-height: 36px;
  }
  .back__title span { display: block; padding-left: 18px; }
  .ribbon {
    position: absolute; right: -70px; top: 40px; width: 300px; height: 62px;
    background: var(--blue); transform: rotate(38deg);
    color: var(--white); font-family: "Kanit", sans-serif; font-size: 17px;
    line-height: 19px; text-align: center; padding-top: 11px;
  }
  .back__body { position: absolute; left: 34px; top: 132px; width: 410px; }
  .feature { margin-bottom: 10px; }
  .feature__title {
    font-family: "Kanit", sans-serif; font-weight: 500; color: var(--blue);
    font-size: 19px; line-height: 22px;
  }
  .feature__text { font-size: 14px; line-height: 18px; }
  .feature__text em { font-style: normal; color: var(--blue); font-weight: 700; }
  .feature--big .feature__title { font-size: 25px; line-height: 27px; font-weight: 600; color: var(--navy); }
  .divider { height: 3px; background: var(--teal); margin: 6px 0 8px; }

  .badge { position: absolute; right: 30px; top: 150px; width: 220px; height: 220px; }
  .badge__text {
    position: absolute; inset: 0; display: flex; align-items: center; justify-content: center;
    text-align: center; color: var(--white); font-family: "Kanit", sans-serif;
    font-weight: 500; font-size: 23px; line-height: 25px;
  }

  .back__cta {
    position: absolute; left: 0; bottom: 20px; width: 100%; height: 88px;
    background: var(--teal); color: var(--white); padding: 12px 34px;
    font-size: 16px; line-height: 21px;
  }
  .back__cta strong { font-family: "Kanit", sans-serif; font-weight: 500; }
  .promo {
    display: inline-block; background: var(--white); color: var(--navy);
    font-family: "Kanit", sans-serif; font-weight: 600; padding: 0 10px; margin-right: 8px;
    border-radius: 3px;
  }

  /* Front */
  .front__photo {
    position: absolute; inset: 0;
    background: linear-gradient(160deg, #2c2a25 0%, #5a4632 35%, #7b6650 55%, #3a3934 80%, #22262a 100%);
  }
  .front__tab {
    position: absolute; left: 250px; top: 0; width: 250px; height: 118px;
    background: var(--paper); border-bottom: 6px solid var(--teal);
    display: flex; align-items: center; justify-content: center;
  }
  .brand-name {
    font-family: "Kanit", sans-serif; font-weight: 600; color: var(--blue);
    font-size: 62px; letter-spacing: 1px;
  }
  .front__motto {
    position: absolute; left: 40px; top: 170px;
    font-family: "Kanit", sans-serif; font-weight: 600; color: var(--white);
    font-size: 64px; line-height: 66px;
  }
  .front__motto span { display: block; padding-left: 30px; }
  .front__web {
    position: absolute; right: 0; bottom: 0; width: 330px; height: 62px;
    background: var(--teal); color: var(--white);
    font-family: "Kanit", sans-serif; font-size: 26px;
    display: flex; align-items: center; justify-content: center;
    clip-path: polygon(30px 0, 100% 0, 100% 100%, 0 100%);
  }
</style>
</head>
<body>

<section class="card card--back">
  <header class="back__header">
    <h2 class="back__title">Modern technology solution<span>for beverage stocktaking</span></h2>
  </header>
  <div class="ribbon">Smart &amp; simple<br>reporting system</div>

  <div class="back__body">
    <div class="feature">
      <h3 class="feature__title">Accurate &amp; effective stocktaking</h3>
      <p class="feature__text">Swift measuring with 99% accuracy makes stocktaking significantly quicker and more cost effective <em>(or cost optimising)</em>.</p>
    </div>
    <div class="feature feature--big">
      <h3 class="feature__title">Data availability –<br>everywhere, anytime</h3>
    </div>
    <div class="divider"></div>
    <div class="feature">
      <h3 class="feature__title">Software solution supported by hardware tools</h3>
      <p class="feature__text">QRVLN system is based on universally accessible platforms – smartphones, PCs, and laptops.</p>
    </div>
  </div>

  <div class="badge">
    <svg width="220" height="220" viewBox="0 0 220 220" aria-hidden="true">
      <polygon fill="var(--blue)" points="215,110 196.3,127.2 207,150.2 183.1,158.9 184.2,184.2 158.9,183.1 150.2,207 127.2,196.3 110,215 92.8,196.3 69.8,207 61.1,183.1 35.8,184.2 36.9,158.9 13,150.2 23.7,127.2 5,110 23.7,92.8 13,69.8 36.9,61.1 35.8,35.8 61.1,36.9 69.8,13 92.8,23.7 110,5 127.2,23.7 150.2,13 158.9,36.9 184.2,35.8 183.1,61.1 207,69.8 196.3,92.8"/>
    </svg>
    <p class="badge__text">Useful<br>functions<br>help stock<br>managing at<br>your bar</p>
  </div>

  <footer class="back__cta">
    <p><strong>Find us on qrvln-example.com</strong> and try QRVLN with a one-month free trial.</p>
    <p><span class="promo">QRVLN50</span>Claim your 50% off discount with above promo code</p>
  </footer>
</section>

<section class="card card--front">
  <div class="front__photo" role="img" aria-label="Photo of a bar back shelf lined with liquor bottles under warm lights"></div>
  <div class="front__tab"><span class="brand-name">qrvln</span></div>
  <h1 class="front__motto">Modern beverage<span>stocktaking</span></h1>
  <div class="front__web">www.qrvln-example.com</div>
</section>

</body>
</html>
```